Innovative Consulting Firm Needs New Business Cards and Stationary

Our Innovative Consulting Firm, Larkfield Consulting, is in need of new business cards and stationary designs. We want two-sided cards that incorporate our logo, which is attached. We are looking for something not too formal, but is professional and slick.

Card should have the following information:
Name (ex. Tom Bradley)
Title (ex. Manager)
Address (ex. 24680 Cedar Lane)
Address 2 (ex. Suite 100)
City
State
Zip Code
Mobile
Email

The card should also have our website: www.larkfieldconsulting.example

Industry/Entity Type

Management Consulting

Contact Information for Business Card

Name (ex. Tom Bradley)
Title (ex. Manager)
Address 2 (ex. Suite 100)
City
State
Zip Code
Mobile
Email

Font styles to use
Sans Serif

Requirements
Must have
• The colors on the card must match the colors in the logo. The exact color codes are attached in a pdf.
Nice to have
• The Company's Tagline is "Focused on your Future". This might be nice to incorporate, but not necessary.

```html
<!DOCTYPE html>
<html lang="en">
<head>
<meta charset="utf-8">
<title>Larkfield Consulting – Business Cards</title>
<link href="https://fonts.googleapis.com/css2?family=Open+Sans:wght@400;600;700&display=swap" rel="stylesheet">
<style>
  :root {
    --brand-blue: #1f64a0;
    --brand-blue-deep: #1a5690;
    --brand-yellow: #f2c522;
    --card-white: #f7f7f5;
    --ink-light: #ffffff;
    --ink-muted: #dce8f3;
    --page-bg: #e9e6e0;
  }
  * { box-sizing: border-box; margin: 0; padding: 0; }
  html, body { width: 1200px; height: 780px; overflow: hidden; }
  body {
    background: var(--page-bg);
    font-family: "Open Sans", Arial, sans-serif;
    position: relative;
  }
  .card {
    position: absolute;
    top: 235px;
    width: 540px;
    height: 310px;
    border-radius: 4px;
    overflow: hidden;
    box-shadow: 0 6px 18px rgba(0,0,0,.18);
  }
  /* Front card */
  .card-front { left: 40px; background: var(--card-white); }
  .front-brand {
    height: 118px;
    display: flex;
    align-items: center;
    justify-content: center;
  }
  .wordmark {
    color: var(--brand-blue);
    font-weight: 600;
    font-size: 34px;
    letter-spacing: .5px;
  }
  .name-band {
    height: 34px;
    background: var(--brand-yellow);
    display: flex;
    align-items: center;
    padding-left: 150px;
    color: var(--ink-light);
    font-size: 16px;
  }
  .name-band .person { font-weight: 700; }
  .name-band .divider { margin: 0 8px; opacity: .9; }
  .name-band .role { font-weight: 400; font-size: 14px; }
  .contact-band {
    height: 118px;
    background: var(--brand-blue);
    display: flex;
    align-items: center;
    justify-content: center;
    gap: 24px;
    color: var(--ink-light);
    font-size: 13px;
    line-height: 1.45;
  }
  .contact-col { display: flex; align-items: flex-start; gap: 8px; }
  .contact-rule { width: 1px; height: 70px; background: rgba(255,255,255,.6); }
  .icon-chip {
    width: 16px; height: 16px; flex: none;
    background: var(--brand-yellow);
    display: flex; align-items: center; justify-content: center;
    margin-top: 2px;
  }
  .front-web {
    height: 40px;
    display: flex;
    align-items: center;
    justify-content: center;
    color: var(--brand-blue);
    font-size: 13px;
  }
  /* Back card */
  .card-back {
    left: 620px;
    background: radial-gradient(circle at 55% 45%, #2a73b2 0%, var(--brand-blue) 45%, var(--brand-blue-deep) 100%);
  }
  .back-brand {
    position: absolute;
    inset: 0 0 34px 0;
    display: flex;
    align-items: center;
    justify-content: center;
  }
  .card-back .wordmark { color: var(--ink-light); font-size: 38px; }
  .back-strip {
    position: absolute;
    left: 0; right: 0; bottom: 0;
    height: 34px;
    background: var(--brand-yellow);
    display: flex;
    align-items: center;
    justify-content: center;
    color: var(--brand-blue-deep);
    font-size: 13px;
  }
</style>
</head>
<body>
  <section class="card card-front">
    <div class="front-brand">
      <span class="wordmark">Larkfield Consulting</span>
    </div>
    <div class="name-band">
      <span class="person">Tom Bradley</span><span class="divider">|</span><span class="role">Manager</span>
    </div>
    <div class="contact-band">
      <div class="contact-col">
        <span class="icon-chip">
          <svg width="11" height="8" viewBox="0 0 11 8"><rect x=".5" y=".5" width="10" height="7" fill="none" stroke="#1f64a0"/><path d="M.5 .5 5.5 4.5 10.5 .5" fill="none" stroke="#1f64a0"/></svg>
        </span>
        <div>tom.bradley@larkfield.example<br>24680 Cedar Lane<br>Suite 100, USA</div>
      </div>
      <span class="contact-rule"></span>
      <div class="contact-col">
        <span class="icon-chip">
          <svg width="10" height="10" viewBox="0 0 10 10"><path d="M2 1 4 1 4.6 3 3.5 4a5 5 0 0 0 2.5 2.5L7 5.4 9 6v2c0 .6-.4 1-1 1A7 7 0 0 1 1 2c0-.6.4-1 1-1z" fill="#1f64a0"/></svg>
        </span>
        <div>+61 555 010 482<br>24680 Cedar Lane<br>Suite 100, USA</div>
      </div>
    </div>
    <div class="front-web">www.larkfieldconsulting.example</div>
  </section>

  <section class="card card-back">
    <div class="back-brand">
      <span class="wordmark">Larkfield Consulting</span>
    </div>
    <div class="back-strip">www.larkfieldconsulting.example</div>
  </section>
</body>
</html>
```